KV Taxidermy

I need business Cards with my logo and a background photo of one of my taxidermy mounts.
I would like a black back drop behind it all and what ever looks best for my contact information (red or white?)
Marcus Pellow
555-218-4907
kvtaxidermy512@mailvex.net
Chatterly page

```html
<!DOCTYPE html>
<html lang="en">
<head>
<meta charset="utf-8">
<title>KV Taxidermy — Business Cards</title>
<link rel="stylesheet" href="https://fonts.googleapis.com/css2?family=Oswald:wght@500;700&family=Open+Sans:wght@400;600&display=swap">
<style>
  :root {
    --backdrop: #e4e2de;
    --card-white: #f7f7f7;
    --card-black: #141414;
    --ink: #1c1c1c;
    --ink-soft: #3a3a3a;
    --mount-light: #d9d6d0;
    --mount-mid: #8d8a85;
    --reverse: #ffffff;
  }
  * { margin: 0; padding: 0; box-sizing: border-box; }
  html, body {
    width: 1200px; height: 942px; overflow: hidden;
    background: var(--backdrop);
  }
  .stage {
    width: 1200px; height: 942px;
    display: flex; flex-direction: column;
    align-items: center; justify-content: center; gap: 56px;
  }
  .card {
    width: 640px; height: 366px;
    position: relative; overflow: hidden;
    border-radius: 4px;
    box-shadow: 0 10px 30px rgba(0,0,0,.18);
  }

  /* Front */
  .card-front { background: var(--card-white); color: var(--ink); }
  .front-brand {
    position: absolute; top: 64px; left: 0; right: 0;
    display: flex; align-items: center; justify-content: center; gap: 10px;
    font-family: "Oswald", sans-serif; font-weight: 700;
    font-size: 30px; letter-spacing: 2px; text-transform: uppercase;
  }
  .brand-mark {
    width: 22px; height: 22px; background: var(--ink);
  }
  .holder-name {
    position: absolute; top: 150px; left: 0; right: 0; text-align: center;
    font-family: "Oswald", sans-serif; font-weight: 700;
    font-size: 30px; letter-spacing: 1px; text-transform: uppercase;
  }
  .name-rule {
    position: absolute; top: 212px; left: 50%;
    width: 40px; height: 3px; margin-left: -20px; background: var(--ink);
  }
  .contact-row {
    position: absolute; bottom: 44px; left: 0; right: 0;
    display: flex; justify-content: center; gap: 34px;
    font-family: "Open Sans", sans-serif; font-size: 15px; color: var(--ink-soft);
  }
  .contact-item { display: flex; align-items: center; gap: 8px; }
  .contact-item svg { width: 15px; height: 15px; fill: var(--ink); }
  .social-square { width: 13px; height: 13px; background: var(--ink); }

  /* Back */
  .card-back { background: var(--card-black); }
  .mount-photo {
    position: absolute; left: 70px; top: -20px; width: 420px; height: 420px;
    border-radius: 45% 40% 50% 45%;
    background: radial-gradient(ellipse at 45% 45%, var(--mount-light) 0%, var(--mount-mid) 45%, rgba(20,20,20,0) 72%);
    opacity: .55;
  }
  .back-brand {
    position: absolute; top: 50%; left: 50%;
    transform: translate(-50%, -50%);
    display: flex; align-items: center; gap: 12px;
    font-family: "Oswald", sans-serif; font-weight: 700;
    font-size: 38px; letter-spacing: 3px; text-transform: uppercase;
    color: var(--reverse); white-space: nowrap;
  }
  .back-brand .brand-mark { width: 26px; height: 26px; background: var(--reverse); }
</style>
</head>
<body>
<main class="stage">
  <section class="card card-front">
    <div class="front-brand"><span class="brand-mark"></span>KV Taxidermy</div>
    <h1 class="holder-name">Marcus Pellow</h1>
    <div class="name-rule"></div>
    <div class="contact-row">
      <span class="contact-item">
        <svg viewBox="0 0 16 16" aria-hidden="true"><path d="M3.6 1.2l2.3 2.6-1.3 1.7c.9 2 2.3 3.4 4.3 4.4l1.7-1.3 2.6 2.3-1.2 2.6C7 13.3 2.8 9 1.1 3.1z"/></svg>
        555-218-4907
      </span>
      <span class="contact-item">
        <svg viewBox="0 0 16 16" aria-hidden="true"><path d="M1 3h14v10H1zM2.5 4.5v.4L8 9l5.5-4.1v-.4z" fill-rule="evenodd"/></svg>
        kvtaxidermy512@mailvex.net
      </span>
      <span class="contact-item"><span class="social-square"></span>Chatterly page</span>
    </div>
  </section>

  <section class="card card-back">
    <div class="mount-photo" role="img" aria-label="Photo of a white ram taxidermy mount on a rock against black"></div>
    <div class="back-brand"><span class="brand-mark"></span>KV Taxidermy</div>
  </section>
</main>
</body>
</html>
```